Plumbing Business Card Design

our business is a plumbing business.
we would like to see designs with our LOGO featured and then either purple or black writing with a white back ground
or black back ground with white or purple writing or even a purple card!
one option we would love to see is if you could get the KTW letters away from the white background ( it is currently in a white box as a jpeg )it is currently on and overlay it onto black.
FRONT
KTW image to be displayed on the front, please use the attached picture. ( you can remove the email address and mobile number from the botttom and re write it in different font or in a different place on the front.
Directly under the large KTW we would like the words Copper Linton Plumbing.
could be spread out like this C O P P E R L I N T O N
P L U M B I N G
We really are open to suggestions though!
Also on the front of the card we could like our little catch phrase somewhere Borra's Trusted Plumber

we dont want in plumbing pictures or photos but we are open to swirl across the card or water movement or droplets.

BACK
These services need to be dot pointed or listed on the back
Hot & Cold Water Services
Gas Fitting
Bathroom & Kitchen Renovations
Metal Roofing & Guttering
New Homes & Extensions
Hot Water Service Changeovers
Drainage & Stormwater Works
All General Plumbing & Maitenance

in smaller writing or down the bottom of the card on the back please display write this Lic. No 492318

Contact Information for Business Card

Reid Linton
Mobile: 0427 316 902
email: copperlintonplumbing@mailvane.example
FInd Us on Facebook Copper Linton Plumbing ( with the f symbol ) either on the front or the back

```html
<!DOCTYPE html>
<html lang="en">
<head>
<meta charset="utf-8">
<title>Copper Linton Plumbing – Business Card</title>
<link href="https://fonts.googleapis.com/css2?family=Source+Sans+3:wght@400;600;700&display=swap" rel="stylesheet">
<style>
  :root {
    --stage: #6b6b6b;
    --card-white: #ffffff;
    --card-black: #000000;
    --brand-blue: #3a78c0;
    --brand-purple: #6a4fa3;
    --service-purple: #7d5fc6;
    --ink: #333333;
  }
  * { margin: 0; padding: 0; box-sizing: border-box; }
  html, body { width: 1200px; height: 900px; overflow: hidden; }
  body {
    background: var(--stage);
    font-family: "Source Sans 3", "Myriad Pro", Arial, sans-serif;
    position: relative;
  }
  .card {
    position: absolute;
    top: 170px;
    width: 347px;
    height: 561px;
    text-align: center;
  }
  .card--front { left: 246px; background: var(--card-white); }
  .card--back { left: 631px; background: var(--card-black); }

  .tab {
    position: absolute;
    left: 101px;
    width: 144px;
    height: 29px;
    background: var(--brand-purple);
  }
  .tab--top { top: 0; }
  .tab--bottom { bottom: 0; }

  .brand {
    position: absolute;
    left: 0; right: 0;
    top: 86px;
  }
  .brand__mark {
    font-weight: 700;
    font-size: 118px;
    line-height: 1;
    letter-spacing: 14px;
    color: var(--brand-blue);
    padding-left: 14px;
  }
  .brand__name {
    margin-top: 10px;
    font-weight: 700;
    font-size: 20px;
    letter-spacing: 0.3px;
    color: var(--brand-blue);
  }
  .card--back .brand { top: 90px; }

  .contact {
    position: absolute;
    left: 0; right: 0;
    top: 296px;
    color: var(--ink);
  }
  .contact__name {
    font-weight: 600;
    font-size: 21px;
    color: var(--brand-purple);
    margin-bottom: 24px;
  }
  .contact__list { list-style: none; font-size: 15.5px; line-height: 20.5px; }
  .contact__list li { display: flex; justify-content: center; align-items: center; gap: 6px; }
  .contact__icon { width: 11px; height: 11px; flex: none; }
  .contact__licence { margin-top: 17px; font-size: 17px; }

  .services {
    position: absolute;
    left: 0; right: 0;
    top: 306px;
    list-style: none;
    font-weight: 600;
    font-size: 15.5px;
    line-height: 20.2px;
    color: var(--service-purple);
  }
</style>
</head>
<body>

<section class="card card--front" aria-label="Business card front">
  <div class="tab tab--top"></div>
  <div class="brand">
    <div class="brand__mark">KTW</div>
    <div class="brand__name">COPPER LINTON PLUMBING</div>
  </div>
  <div class="contact">
    <p class="contact__name">REID LINTON</p>
    <ul class="contact__list">
      <li>
        <svg class="contact__icon" viewBox="0 0 11 11" aria-hidden="true">
          <rect x="2.5" y="0.5" width="6" height="10" rx="1.2" fill="none" stroke="var(--brand-purple)" stroke-width="1.3"/>
          <circle cx="5.5" cy="8.6" r="0.7" fill="var(--brand-purple)"/>
        </svg>
        0427 316 902
      </li>
      <li>
        <svg class="contact__icon" viewBox="0 0 11 11" aria-hidden="true">
          <rect x="0.5" y="2.5" width="10" height="7" fill="var(--brand-purple)"/>
          <path d="M0.8 2.8 L5.5 6.5 L10.2 2.8" fill="none" stroke="#fff" stroke-width="0.9"/>
        </svg>
        copperlintonplumbing@mailvane.example
      </li>
      <li>
        <svg class="contact__icon" viewBox="0 0 11 11" aria-hidden="true">
          <rect x="1" y="1" width="9" height="9" rx="1.5" fill="var(--brand-purple)"/>
        </svg>
        CopperLintonPlumbing
      </li>
    </ul>
    <p class="contact__licence">LIC. NO 492318</p>
  </div>
  <div class="tab tab--bottom"></div>
</section>

<section class="card card--back" aria-label="Business card back">
  <div class="brand">
    <div class="brand__mark">KTW</div>
    <div class="brand__name">COPPER LINTON PLUMBING</div>
  </div>
  <ul class="services">
    <li>Hot &amp; Cold Water Services</li>
    <li>Gas Fitting</li>
    <li>Bathroom &amp; Kitchen Renovations</li>
    <li>Metal Roofing &amp; Guttering</li>
    <li>New Homes &amp; Extensions</li>
    <li>Hot Water Service Changeovers</li>
    <li>Drainage &amp; Stormwater Works</li>
    <li>All General Plumbing &amp; Maitenance</li>
  </ul>
</section>

</body>
</html>
```